Zielgruppe
Bestattungen Angehörige von Verstorbenen
Bestattungshaus Lindmark
Ahornsteig 7
61479 Lindmark
www.bestattungshaus-lindmark.de
info@bestattungshaus-lindmark.de
Tel: 06173 / 4820517
Mobil: 0152 / 83740162 24 Std Erreichbarkeit
Aufgabenstellung
Über mich
Mein Name ist Wolfgang Brenner, ich kann auf eine langjährige Berufserfahrung als Humanbestatter zurückblicken.
Die Versorgung und Bestattung eines Verstobenen, ist für Angehörige ein sehr wichtiger Aspekt.
Daher habe ich es mir zur Aufgabe gemacht, Sie auf diesem Weg in Ruhe und mit Genauigkeit zu begleiten.
Was Sie im Trauerfall beachten müssen
Bitte Bewahren Sie ruhe.
Jeder Trauerfall erfordert gewisse Maßnahmen die man treffen muss da diese im Bestattungsgesetzt Festgehalten sind.
Bitte informieren Sie uns Zeitnah um alles wichtige vorab zu besprechen und den Ablauf der Überführung des Verstorbenen zu klären.
Ein ausführliches Gespräch erfolgt zu einen späteren Zeitpunkt wo alle weiteren Fragen Ihrerseits, der Ablauf der Trauerfeier und oder Beisetzung geplant werden.
Verstirb ein Mensch zuhause
Müssen Sie zunächst den Hausarzt, Hausärztlichenvertretungsdienst (116 117 ),
oder den Rettungsdienst ( 112 ) informieren. Dieser wird dann nach der ersten Leichenschau den Totenschein ausstellen, der für den weiteren Ablauf mit uns sehr wichtig ist.
Tritt der Tod jedoch im Krankenhaus,
Pflege & Altenheim ein kümmert sich die dortige Verwaltung um die Formalitäten.
Unsere Leistungen für Sie
Gerne übernehmen wir für Sie folgende Aufgaben:
Persönliche Beratung und Betreuung Überführung im In- und Ausland
Erledigung sämtlicher Formalitäten (z.B. Todesbescheinigung, Sterbeurkunde.)
Versorgung des Verstorbenen nach DIN EN 15017
Aufbahrung & Abschiednahme in unseren Räumlichkeiten.
Trauerdrucksachen ,Traueranzeigen
Beratung bei der Wahl der Bestattungsform und des Ortes der Beisetzung.
Alle Bestattungsformen und Grab Arten sind bei uns möglich
Terminabsprachen mit Pfarrer/Trauerrednern, Friedhofsverwaltung
Individuelle Gestaltung, Organisation und Betreuung der Trauer P..

```html
<!DOCTYPE html>
<html lang="de">
<head>
<meta charset="utf-8">
<title>Bestattungshaus Lindmark – Flyer</title>
<link rel="stylesheet" href="https://fonts.googleapis.com/css2?family=Outfit:wght@300;400;500;600&family=Crimson+Text:ital,wght@1,600&display=swap">
<style>
:root{
  --bg:#8f8b89;
  --paper:#fdfbf7;
  --beige:#f3e5c9;
  --beige-soft:#f6eedf;
  --sand:#e2d2b2;
  --cover-grey:#dedcda;
  --panel-grey:#ecebea;
  --ink:#4b4848;
  --ink-strong:#3b3838;
  --brand-grey:#6b6562;
}
*{box-sizing:border-box;margin:0;padding:0}
html,body{width:1200px;height:729px;overflow:hidden}
body{background:var(--bg);font-family:"Outfit",sans-serif;color:var(--ink);position:relative}
.spread{position:absolute;top:34px;display:flex;height:660px;box-shadow:0 6px 18px rgba(0,0,0,.25)}
.spread--outside{left:16px}
.spread--inside{left:612px}
.panel{position:relative;width:286px;height:660px;overflow:hidden;background:var(--paper)}
.panel + .panel{border-left:1px solid #e4e1dc}
.shape{position:absolute;left:0;top:0;width:100%;height:100%}
.photo{position:absolute}

/* back panel */
.quote{position:absolute;left:20px;top:104px;width:118px;font-family:"Crimson Text",serif;font-style:italic;font-weight:600;font-size:15px;line-height:18.5px;color:var(--ink)}
.quote-author{position:absolute;left:20px;top:203px;font-size:7px;color:var(--ink)}
.portrait{left:160px;top:36px;width:110px;height:174px;background:linear-gradient(180deg,#d9d8d6 0%,#c9c7c4 45%,#3e3f44 70%,#2f3034 100%)}
.intro{position:absolute;left:20px;top:228px;width:252px;font-size:9.6px;line-height:16.5px;font-weight:300}
.intro p{margin-bottom:6px}
.intro strong{font-weight:500}
.contact{position:absolute;left:20px;top:436px;font-size:9.4px;line-height:16px;font-weight:300}
.contact-name{font-weight:500;font-size:11.8px;margin-bottom:2px}
.phones{margin-top:4px;font-size:11.5px;line-height:16px;font-weight:500}
.phones span.label{display:inline-block;width:50px}
.phones small{font-size:8px;font-weight:300}
.partner{position:absolute;left:20px;top:576px;width:255px;height:56px;background:var(--paper);display:flex;align-items:center;gap:44px;padding-left:12px;font-size:8.5px;line-height:12px;font-weight:300}
.partner-mark{display:flex;align-items:center;gap:6px;font-size:12px;font-weight:500;color:var(--ink)}
.partner-mark i{display:block;width:16px;height:16px;border-radius:50%;background:var(--sand)}

/* cover */
.panel--cover{background:var(--cover-grey)}
.cover-photo{left:8px;top:8px;width:270px;height:462px;background:radial-gradient(ellipse at 50% 30%,#cbbba6 0%,#9c8e80 45%,#5e5957 100%)}
.brand{position:absolute;left:70px;width:200px;top:526px;text-align:center;font-weight:300;color:var(--brand-grey);font-size:22px;line-height:24px;letter-spacing:.4px}

/* services */
.panel--services{background:var(--panel-grey)}
.services{position:absolute;left:18px;top:20px;width:256px}
.services h2{font-size:14.5px;font-weight:500;color:var(--ink-strong);margin-bottom:12px}
.services .lead{font-size:9.6px;font-weight:300;margin-bottom:4px}
.services ul{list-style:none;font-size:9.6px;line-height:13px;font-weight:300}
.services li{position:relative;padding-left:6px;margin-bottom:5px}
.services li::before{content:"•";position:absolute;left:0}
.services .closing{margin-top:16px;font-size:12px;line-height:14px;font-weight:500;color:var(--ink-strong)}
.deco-photo{left:18px;top:450px;width:252px;height:180px;background:linear-gradient(180deg,#d9d2c2 0%,#c9bfa8 55%,#9a6a45 78%,#7a4f33 100%)}

/* advice */
.room-photo{left:16px;top:18px;width:254px;height:156px;background:linear-gradient(160deg,#efeeea 0%,#c9c3b9 40%,#8a6b52 70%,#b7a58c 100%)}
.advice{position:absolute;left:16px;top:192px;width:258px;font-size:9.4px;line-height:15.5px;font-weight:300}
.advice h2{font-size:14.5px;font-weight:500;color:var(--ink-strong);margin-bottom:16px}
.advice p{margin-bottom:13px}
.advice strong{font-weight:500}
</style>
</head>
<body>

<section class="spread spread--outside">
  <article class="panel panel--back">
    <svg class="shape" viewBox="0 0 286 660" preserveAspectRatio="none" aria-hidden="true">
      <path d="M6 6H280V170C260 160 250 90 200 80C150 70 120 55 80 70C50 80 25 100 6 115Z" fill="var(--beige)"/>
      <path d="M280 420C270 470 255 520 245 560V660H150C200 640 240 560 280 420Z" fill="var(--beige)"/>
    </svg>
    <p class="quote">Was man tief in seinem Herzen besitzt, kann man nicht durch den Tod verlieren.</p>
    <p class="quote-author">Johann F. Hollmann</p>
    <div class="photo portrait" role="img" aria-label="Porträtfoto des Bestatters im dunklen Anzug"></div>
    <div class="intro">
      <p>Mein Name ist <strong>Wolfgang Brenner</strong>, ich kann auf eine langjährige Berufserfahrung als <strong>Humanbestatter</strong> zurückblicken.</p>
      <p>Die Versorgung und Bestattung eines Verstobenen, ist für Angehörige ein sehr wichtiger Aspekt.</p>
      <p>Daher habe ich es mir zur Aufgabe gemacht, Sie auf diesem Weg in Ruhe und mit Genauigkeit zu begleiten.</p>
    </div>
    <div class="contact">
      <p class="contact-name">Bestattungshaus Lindmark</p>
      <p>Ahornsteig 7</p>
      <p>61479 Lindmark</p>
      <p>www.bestattungshaus-lindmark.de</p>
      <p>info@bestattungshaus-lindmark.de</p>
      <div class="phones">
        <p><span class="label">Telefon:</span>06173 / 4820517</p>
        <p><span class="label">Mobil:</span>0152 / 83740162 <small>(24h erreichbar)</small></p>
      </div>
    </div>
    <div class="partner">
      <p>Wir sind Partner<br>von Waldruhe</p>
      <p class="partner-mark"><i></i>Waldruhe</p>
    </div>
  </article>

  <article class="panel panel--cover">
    <div class="photo cover-photo" role="img" aria-label="Unscharfes Foto einer Engelsfigur vor einem Herz aus Zweigen"></div>
    <svg class="shape" viewBox="0 0 286 660" preserveAspectRatio="none" aria-hidden="true">
      <path d="M0 400C40 360 80 375 130 400C180 425 230 420 286 390V660H0Z" fill="var(--cover-grey)"/>
      <path d="M0 660V625C30 595 80 585 130 605C170 620 200 625 230 615C255 607 275 615 286 625V660Z" fill="var(--sand)"/>
    </svg>
    <div class="brand">
      <p>Bestattungshaus</p>
      <p>Lindmark</p>
    </div>
  </article>
</section>

<section class="spread spread--inside">
  <article class="panel panel--services">
    <svg class="shape" viewBox="0 0 286 660" preserveAspectRatio="none" aria-hidden="true">
      <path d="M6 6H280V250C250 320 200 360 140 365C80 370 30 360 6 345Z" fill="var(--beige-soft)"/>
    </svg>
    <div class="services">
      <h2>Unsere Leistungen für Sie</h2>
      <p class="lead">Gerne übernehmen wir für Sie folgende Aufgaben:</p>
      <ul>
        <li>Persönliche Beratung und Betreuung Überführung im In- und Ausland</li>
        <li>Erledigung sämtlicher Formalitäten (z.B. Todesbescheinigung, Sterbeurkunde.)</li>
        <li>Versorgung des Verstorbenen nach DIN EN 15017</li>
        <li>Aufbahrung &amp; Abschiednahme in unseren Räumlichkeiten.</li>
        <li>Trauerdrucksachen ,Traueranzeigen</li>
        <li>Beratung bei der Wahl der Bestattungsform und des Ortes der Beisetzung.</li>
        <li>Alle Bestattungsformen und Grab Arten sind bei uns möglich</li>
        <li>Terminabsprachen mit Pfarrer/Trauerrednern, Friedhofsverwaltung</li>
        <li>Individuelle Gestaltung, Organisation und Betreuung der Trauer Planung und Durchführung von Trauermusik oder auch die Bestellung eines Organisten</li>
        <li>Bestattungsvorsorge /Bestattungstreuhand</li>
      </ul>
      <p class="closing">Bei allen weiteren Fragen sprechen Sie uns an.<br>Wir sind gern für Sie da.</p>
    </div>
    <div class="photo deco-photo" role="img" aria-label="Dekoration mit Kerzen, Gräsern und Holzherz auf Holzboden"></div>
  </article>

  <article class="panel panel--advice">
    <svg class="shape" viewBox="0 0 286 660" preserveAspectRatio="none" aria-hidden="true">
      <path d="M286 380C250 420 240 520 230 660H286Z" fill="var(--beige-soft)"/>
      <path d="M0 600C40 610 70 630 90 660H0Z" fill="var(--beige-soft)"/>
    </svg>
    <div class="photo room-photo" role="img" aria-label="Beratungsraum mit Holztisch und Urnenregal"></div>
    <div class="advice">
      <h2>Was Sie im Trauerfall beachten müssen</h2>
      <p><strong>Bitte Bewahren Sie Ruhe.</strong><br>Jeder Trauerfall erfordert gewisse Maßnahmen die man treffen muss, da diese im Bestattungsgesetz festgehalten sind.</p>
      <p><strong>Bitte informieren Sie uns zeitnah</strong> um alles Wichtige vorab zu besprechen und den Ablauf der Überführung des Verstorbenen zu klären.</p>
      <p><strong>Ein ausführliches Gespräch erfolgt zu einem späteren Zeitpunkt</strong>, wo alle weiteren Fragen Ihrerseits, der Ablauf der Trauerfeier und oder Beisetzung geplant werden.</p>
      <p>Verstirbt ein Mensch zuhause, müssen Sie zunächst den <strong>Hausarzt, Hausärztlichenvertretungsdienst ( 116 117 ), oder den Rettungsdienst ( 112 )</strong> informieren.<br>Dieser wird dann nach der ersten Leichenschau den Totenschein ausstellen, der für den weiteren Ablauf mit uns sehr wichtig ist.</p>
      <p>Tritt der Tod jedoch im Krankenhaus, Pflege &amp; Altenheim ein kümmert sich die dortige Verwaltung um die Formalitäten.</p>
    </div>
  </article>
</section>

</body>
</html>
```